Law Firm Needs a new Website Design

We need a new website design for our law firm located in Manhattan (Law Offices of Tobias R. Venkland, PLLC).
We have an existing logo that we will to continue using, which can be found in www.VenklandLaw.example.
The plain badge shape, plain badge shape Logo should also be reflected near the bottom of the Home page.
The website will be 6 pages.

Deliverables:
I want a
1) home page,
2) About Us/Practice Areas page,
3) attorneys,
4) News and Articles page, and
5) Contact and Directions/Privacy Policy page.

The colors of my logo should be in the website.
I also like a touch of black and red.

The website should project "excellence."
We seek to provide the highest quality legal services.
We handle estate planning, wills, trusts, planning for people with disabilities, asset protection and preservation, Medicaid planning, hospital safe discharge, nursing home placement, powers of attorney, health care proxies, living wills, guardianships, probate, estate administration and related litigation.

I would like the colors of my Logo used (including shading where appropriate).
I also want some black on the borders and/or bottom and some red touches throughout the page.

My Logo should appear everywhere that "Law Offices Of Tobias R. Venkland, PLLC" appears.
I want the badges for Prime counsel, plain badge shape, Top Legal Practices, and ZELQ on the Home page.
I do not want too much text on the home page.

We would also like the website to have coding.
The final design should also communicate quality, expertise and stability.
Great start so far by the people who submitted designs.
Thank you.

Industry/Entity Type

Law Firm

Coding

Coded - Design and coding required

Number of Pages Required

5+ page

Colors
3276b5
ec1f27
474747

Requirements
Must have
• Please use my logo each time you mention Law Offices of Tobias R. Venkland, PLLC. Please include the Primecounsel, plain badge shape, Top Legal Practices and plain badge shape rating Badges on the web home page. I only wish to be contacted by phone. I am not including testimonials and am only using the New York City address.
Nice to have
• Prefer illustrations to photos regarding practice areas
Should not have
• Testimonials, contact me by email, free consultation.

```html
<!DOCTYPE html>
<html lang="en">
<head>
<meta charset="utf-8">
<title>Law Offices of Tobias R. Venkland, PLLC</title>
<link rel="stylesheet" href="https://fonts.googleapis.com/css2?family=Roboto:wght@300;400;500;700&family=Open+Sans:wght@400;600&display=swap">
<style>
:root{
  --blue:#3a5bb5;
  --blue-dark:#26388a;
  --blue-deep:#1e2f78;
  --nav:#3550a8;
  --ink:#474747;
  --muted:#6a6a6a;
  --light:#f0f0f0;
  --white:#ffffff;
  --footer:#1f1f1f;
  --footer-bar:#141414;
  --red:#ec1f27;
}
*{box-sizing:border-box;margin:0;padding:0}
html,body{width:1200px;height:3152px;overflow:hidden}
body{font-family:"Open Sans",Arial,sans-serif;color:var(--ink);background:var(--white);position:relative}
.wrap{width:1000px;margin:0 auto;position:relative;height:100%}
section,header,nav,footer{position:relative;width:1200px;overflow:hidden}
h1,h2,h3,h4{font-family:"Roboto",Arial,sans-serif;font-weight:400}

/* header */
.site-header{height:126px}
.brand{position:absolute;left:0;top:28px;display:flex;align-items:center;gap:14px}
.brand-square{width:52px;height:52px;background:var(--blue-dark)}
.brand-name{font-family:"Roboto",Arial,sans-serif;color:var(--blue-deep);line-height:1.1}
.brand-name small{display:block;font-size:15px;text-align:center}
.brand-name strong{display:block;font-size:27px;font-weight:400;letter-spacing:.5px}
.brand-name em{display:block;font-style:normal;font-size:13px;text-align:center}
.contact-top{position:absolute;left:540px;top:34px;display:flex;gap:18px;align-items:center;font-size:14px;color:var(--muted);line-height:1.7}
.social{position:absolute;right:0;top:44px;display:flex;gap:6px}
.social span{width:22px;height:22px;border-radius:50%;background:var(--blue)}
.social span:nth-child(3){background:var(--red)}
.social span:nth-child(4){background:#9a9a9a}

/* nav */
.main-nav{height:54px;background:linear-gradient(var(--nav),var(--blue-dark))}
.main-nav ul{list-style:none;display:flex;height:54px}
.main-nav li{font-family:"Roboto",Arial,sans-serif;font-size:13px;color:var(--white);padding:0 26px;line-height:54px;letter-spacing:.3px}
.main-nav li.active{background:var(--blue-deep)}

/* hero */
.hero{height:496px;background:linear-gradient(180deg,#5b5a5a 0%,#7a5e3c 35%,#4c4a48 70%,#2d3038 100%)}
.hero-content{position:absolute;left:0;right:0;top:110px;text-align:center;color:var(--white)}
.hero-mark{width:70px;height:70px;background:var(--white);margin:0 auto 24px}
.hero h1{font-size:38px;line-height:1.15;font-weight:400}
.hero p{font-size:14px;margin-top:14px;line-height:1.5}
.hero-arrow{position:absolute;top:220px;width:34px;height:34px;border-radius:50%;background:#111}
.hero-arrow.prev{left:34px}.hero-arrow.next{right:34px}
.hero-arrow svg{display:block;margin:9px auto}

/* about */
.about{height:416px;background:var(--white)}
.about-photo{position:absolute;left:0;top:70px;width:372px;height:292px;border:1px solid #d8d8d8;padding:6px;background:var(--white)}
.about-photo div{width:100%;height:100%;background:linear-gradient(135deg,#cfd6df,#8b9bb1 55%,#3b4a67)}
.about-text{position:absolute;left:464px;top:76px;width:530px}
.section-title{display:flex;align-items:center;gap:16px;font-family:"Roboto",Arial,sans-serif;color:var(--blue-deep);font-size:26px;line-height:1.15}
.section-title i{width:44px;height:44px;background:var(--blue-dark);display:block}
.about-text p{font-size:10.5px;line-height:1.75;color:var(--muted);margin-top:24px}
.about-text p+p{margin-top:12px}

/* practice */
.practice{height:504px;background:var(--light)}
.centered-title{text-align:center;font-family:"Roboto",Arial,sans-serif;color:var(--blue-deep);font-size:30px}
.divider{display:flex;align-items:center;justify-content:center;gap:10px;margin-top:8px}
.divider span{width:70px;height:1px;background:#9aa6c8}
.divider b{width:12px;height:12px;background:var(--blue-dark);transform:rotate(45deg)}
.practice .centered-title{padding-top:50px}
.practice-intro{text-align:center;font-size:11.5px;line-height:1.8;color:var(--muted);margin:22px auto 0;width:920px}
.areas{display:flex;justify-content:space-between;margin-top:28px;width:1000px}
.area{width:230px;text-align:center}
.area-icon{width:130px;height:130px;margin:0 auto;display:block}
.area h3{font-size:15px;color:var(--ink);margin-top:20px;letter-spacing:.3px}
.area p{font-size:11.5px;line-height:1.7;color:var(--muted);margin-top:8px}

/* quote */
.quote{height:262px;background:linear-gradient(135deg,#2d4aa0,#24409a 50%,#1d3483)}
.quote blockquote{width:900px;margin:68px auto 0;text-align:center;color:var(--white);font-style:italic;font-size:12.5px;line-height:1.85}
.quote cite{display:block;text-align:center;color:var(--white);font-style:italic;font-size:16px;margin-top:16px}
.quote cite small{display:block;font-size:13px;margin-top:6px}

/* news */
.news{height:444px}
.news .centered-title{padding-top:48px}
.news-grid{display:flex;justify-content:space-between;margin-top:44px}
.news-item{width:310px}
.news-item h3{font-size:15px;line-height:1.75;color:var(--blue);text-transform:uppercase}
.news-item a{display:inline-block;margin-top:16px;font-size:13px;color:var(--ink);text-decoration:underline}
.btn{display:block;width:196px;height:44px;margin:56px auto 0;border:2px solid var(--blue-dark);font-family:"Roboto",Arial,sans-serif;font-size:14px;color:var(--blue-deep);text-align:center;line-height:40px}

/* values */
.values{height:332px;background:linear-gradient(120deg,#3859b0,#4a6cc4 45%,#2f4fa6)}
.values-grid{display:flex;justify-content:space-between;padding-top:68px}
.value{width:230px;text-align:center;color:var(--white)}
.value-icon{width:70px;height:70px;margin:0 auto;border-radius:50%;background:rgba(255,255,255,.85)}
.value h3{font-size:19px;margin-top:16px}
.value p{font-size:12.5px;line-height:1.6;margin-top:6px}

/* badges */
.badges{height:176px}
.badge-row{display:flex;align-items:center;justify-content:space-between;height:176px;padding:0 12px}
.badge{background:#c9ced8}
.badge.tall{width:96px;height:110px;background:linear-gradient(#c4343a,#2b4f9e)}
.badge.wide{width:248px;height:50px;background:#9d7b3a}
.badge.mid{width:288px;height:48px;background:#2d3a8a}
.badge.short{width:196px;height:72px;background:#222}

/* footer */
.site-footer{height:274px;background:var(--footer);color:#cfcfcf}
.footer-brand{position:absolute;left:0;top:62px;width:170px;text-align:center;color:var(--white);font-family:"Roboto",Arial,sans-serif}
.footer-brand i{display:block;width:56px;height:56px;background:var(--white);margin:0 auto 14px}
.footer-brand small{display:block;font-size:11px}
.footer-brand strong{display:block;font-size:15px;font-weight:400;margin-top:2px}
.footer-brand em{display:block;font-style:normal;font-size:10px;margin-top:2px}
.footer-col{position:absolute;top:44px}
.footer-col h4{font-size:17px;color:var(--white);font-weight:500;margin-bottom:16px}
.footer-col li{list-style:none;font-size:11.5px;line-height:23px;text-transform:uppercase;color:#d8d8d8}
.col-areas{left:254px}.col-links{left:560px}.col-contact{left:780px;width:220px}
.col-contact p{font-size:11.5px;line-height:1.8}
.col-contact .row{display:flex;gap:10px;align-items:center;font-size:11.5px;margin-top:8px}
.foot-social{display:flex;gap:6px;margin-top:14px}
.foot-social span{width:24px;height:24px;border-radius:50%;border:1px solid #bbb}
.footer-bar{height:64px;background:var(--footer-bar);color:#cfcfcf;font-size:10.5px}
.footer-bar .left{position:absolute;left:0;top:25px}
.footer-bar .mid{position:absolute;left:488px;top:20px;width:24px;height:24px;background:#d8d8d8}
.footer-bar .right{position:absolute;right:0;top:25px}
</style>
</head>
<body>

<header class="site-header">
  <div class="wrap">
    <div class="brand">
      <span class="brand-square"></span>
      <div class="brand-name">
        <small>Law Offices of</small>
        <strong>TOBIAS R. VENKLAND</strong>
        <em>PLLC</em>
      </div>
    </div>
    <div class="contact-top">
      <svg width="26" height="26" viewBox="0 0 24 24" aria-hidden="true"><path d="M6.6 10.8a15.1 15.1 0 0 0 6.6 6.6l2.2-2.2c.3-.3.7-.4 1-.2 1.1.4 2.3.6 3.6.6.6 0 1 .4 1 1V20c0 .6-.4 1-1 1A17 17 0 0 1 3 4c0-.6.4-1 1-1h3.5c.6 0 1 .4 1 1 0 1.3.2 2.5.6 3.6.1.3 0 .7-.2 1z" fill="#9a9a9a"/></svg>
      <div>218 HALVERN STREET, SUITE 1407 NEW YORK,<br>Call Us : +(212) 555-0148</div>
    </div>
    <div class="social"><span></span><span></span><span></span><span></span></div>
  </div>
</header>

<nav class="main-nav">
  <div class="wrap">
    <ul>
      <li class="active">HOME</li>
      <li>PRACTICE AREAS</li>
      <li>ATTORNEYS</li>
      <li>PRIVACY POLICY</li>
      <li>NEWS</li>
      <li>CONTACT AND DIRECTIONS</li>
    </ul>
  </div>
</nav>

<section class="hero" role="img" aria-label="Aerial photograph of the Manhattan skyline at dusk">
  <span class="hero-arrow prev"><svg width="14" height="16" viewBox="0 0 14 16"><path d="M10 2 4 8l6 6" stroke="#fff" stroke-width="2.5" fill="none"/></svg></span>
  <span class="hero-arrow next"><svg width="14" height="16" viewBox="0 0 14 16"><path d="m4 2 6 6-6 6" stroke="#fff" stroke-width="2.5" fill="none"/></svg></span>
  <div class="hero-content">
    <div class="hero-mark"></div>
    <h1>LAW OFFICES OF TOBIAS<br>R. VENKLAND</h1>
    <p>Lorem ipsum dolor sit amet, consectetur adipiscing elit,<br>sed do eiusmod tempor incididunt ut labore et dolor sit amet,</p>
  </div>
</section>

<section class="about">
  <div class="wrap">
    <div class="about-photo"><div role="img" aria-label="Photograph of a hand pointing to a document on an office desk"></div></div>
    <div class="about-text">
      <h2 class="section-title"><i></i><span>WELCOME TO<br>LAW OFFICES OF TOBIAS R. VENKLAND</span></h2>
      <p>Our firm was founded in 1993 by Tobias R. Venkland, a member of the National Guild of Elder Law Counsel (NGELC) and an elder law practitioner for over 19 years. Our firm is uniquely positioned to provide quality legal advice and representation in regards to estate planning, wills, trusts, planning for people with disabilities, asset protection and preservation, Medicaid planning, hospital safe discharge, nursing home placement, powers of attorney, health care proxies, living wills, guardianships, probate, estate administration and related litigation.</p>
      <p>Our familiarity with entitlement programs such as Medicaid and the statutes and regulations pertaining to them, our sensitivity to the problems and needs of seniors and our access to geriatric care managers enable us to help families preserve their life savings</p>
    </div>
  </div>
</section>

<section class="practice">
  <div class="wrap">
    <h2 class="centered-title">OUR PRACTICE AREAS</h2>
    <div class="divider"><span></span><b></b><span></span></div>
    <p class="practice-intro">We are a law firm &amp; handle estate planning, wills, trusts, planning for people with disabilities, asset protection and preservation, Medicaid planning, hospital safe discharge, nursing home placement, powers of attorney, health care proxies, living wills, guardianships, probate, estate administration and related litigation</p>
    <div class="areas">
      <div class="area">
        <svg class="area-icon" viewBox="0 0 130 130" role="img" aria-label="Estate planning illustration in a blue diamond"><rect x="25" y="25" width="80" height="80" transform="rotate(45 65 65)" fill="#2f4fa6"/></svg>
        <h3>ESTATE PLANNING</h3>
        <p>Estate planning is not just for the very wealthy or for senior citizens and often does not focus solely upon asset</p>
      </div>
      <div class="area">
        <svg class="area-icon" viewBox="0 0 130 130" role="img" aria-label="Probate and estate administration illustration in a blue diamond"><rect x="25" y="25" width="80" height="80" transform="rotate(45 65 65)" fill="#2f4fa6"/></svg>
        <h3>PROBATE &amp; ESTATE ADMIN</h3>
        <p>Although the family is not required to retain an attorney to handle the affairs of a deceased loved one</p>
      </div>
      <div class="area">
        <svg class="area-icon" viewBox="0 0 130 130" role="img" aria-label="Powers of attorney illustration in a blue diamond"><rect x="25" y="25" width="80" height="80" transform="rotate(45 65 65)" fill="#2f4fa6"/></svg>
        <h3>POWERS OF ATTORNEY</h3>
        <p>Regardless of your age, it is prudent to consider what would happen if you were to become incapacitated</p>
      </div>
      <div class="area">
        <svg class="area-icon" viewBox="0 0 130 130" role="img" aria-label="Needs trusts illustration in a blue diamond"><rect x="25" y="25" width="80" height="80" transform="rotate(45 65 65)" fill="#2f4fa6"/></svg>
        <h3>NEEDS TRUSTS</h3>
        <p>Eligibility for certain government benefits, such as Medicaid and Supplemental Security Income (SSI)</p>
      </div>
    </div>
  </div>
</section>

<section class="quote" role="img" aria-label="Blue-tinted photograph of a courthouse behind a quotation">
  <blockquote>“ Lorem ipsum dolor sit amet, consectetur adipiscing elit, sed do eiusmod tempor incididunt ut labore et dolore magna aliqua. Ut enim ad minim veniam, quis nostrud exercitation ullamco laboris nisi ut aliquip ex ea commodo consequat. Duis aute irure dolor in reprehenderit in voluptate velit esse cillum dolore eu fugiat nulla pariatur. Excepteur sint occaecat ”</blockquote>
  <cite>John Doe<small>- Law Offices of Tobias R. Venkland</small></cite>
</section>

<section class="news">
  <div class="wrap">
    <h2 class="centered-title">LATEST NEWS</h2>
    <div class="divider"><span></span><b></b><span></span></div>
    <div class="news-grid">
      <article class="news-item"><h3>Mr. Venkland was selected for the 2015 Top Advocates in America in the practice of elder law</h3><a>Read More</a></article>
      <article class="news-item"><h3>Mr. Venkland was selected for the 2015 Top Advocates in America in the practice of elder law</h3><a>Read More</a></article>
      <article class="news-item"><h3>Mr. Venkland was selected for the 2015 Top Advocates in America in the practice of elder law</h3><a>Read More</a></article>
    </div>
    <span class="btn">VIEW ALL NEWS</span>
  </div>
</section>

<section class="values" role="img" aria-label="Blue-tinted photograph of a handshake across a desk">
  <div class="wrap">
    <div class="values-grid">
      <div class="value"><div class="value-icon"></div><h3>Goals</h3><p>We care about our clients &amp; believe in cultivating long-term relationships. We strive to maintain the</p></div>
      <div class="value"><div class="value-icon"></div><h3>Strategy</h3><p>We care about our clients &amp; believe in cultivating long-term relationships. We strive to maintain the</p></div>
      <div class="value"><div class="value-icon"></div><h3>Approach</h3><p>We care about our clients &amp; believe in cultivating long-term relationships. We strive to maintain the</p></div>
      <div class="value"><div class="value-icon"></div><h3>Negotiations</h3><p>We care about our clients &amp; believe in cultivating long-term relationships. We strive to maintain the</p></div>
    </div>
  </div>
</section>

<section class="badges">
  <div class="wrap">
    <div class="badge-row">
      <span class="badge tall" role="img" aria-label="Top Legal Practices rating badge"></span>
      <span class="badge wide" role="img" aria-label="Prime Counsel rating badge"></span>
      <span class="badge mid" role="img" aria-label="Top Advocates rating badge"></span>
      <span class="badge short" role="img" aria-label="Zelq rating badge"></span>
    </div>
  </div>
</section>

<footer class="site-footer">
  <div class="wrap">
    <div class="footer-brand">
      <i></i>
      <small>Law Offices of</small>
      <strong>TOBIAS R. VENKLAND</strong>
      <em>PLLC</em>
    </div>
    <div class="footer-col col-areas">
      <h4>PRACTICE AREASLINKS</h4>
      <ul><li>Medicaid Planning</li><li>Estate Planning</li><li>Probate and Estate Administration</li><li>Powers of Attorney</li><li>Supplemental Needs Trusts</li><li>Guardianships</li></ul>
    </div>
    <div class="footer-col col-links">
      <h4>QUICK LINKS</h4>
      <ul><li>Home</li><li>Practice Areas</li><li>Contact and Directions</li><li>News</li><li>Privacy Policy</li><li>Attorneys</li></ul>
    </div>
    <div class="footer-col col-contact">
      <h4>CONTACT US</h4>
      <p>Law Offices of Tobias R. Venkland,<br>P.O. BOX 512, ASHGROVE, NY 10093</p>
      <div class="row"><svg width="14" height="14" viewBox="0 0 24 24"><path d="M6.6 10.8a15.1 15.1 0 0 0 6.6 6.6l2.2-2.2c.3-.3.7-.4 1-.2 1.1.4 2.3.6 3.6.6.6 0 1 .4 1 1V20c0 .6-.4 1-1 1A17 17 0 0 1 3 4c0-.6.4-1 1-1h3.5c.6 0 1 .4 1 1 0 1.3.2 2.5.6 3.6.1.3 0 .7-.2 1z" fill="#cfcfcf"/></svg>+1 212.555.0193</div>
      <div class="row"><svg width="14" height="12" viewBox="0 0 24 18"><rect x="1" y="1" width="22" height="16" fill="none" stroke="#cfcfcf" stroke-width="2"/><path d="m1 1 11 9 11-9" fill="none" stroke="#cfcfcf" stroke-width="2"/></svg>info@venklandlaw.example</div>
      <div class="foot-social"><span></span><span></span><span></span><span></span></div>
    </div>
  </div>
</footer>
<div class="footer-bar" style="position:relative;width:1200px">
  <div class="wrap">
    <span class="left">©2014 - 2016 Law Offices of Tobias R. Venkland, PLLC., All Rights Reserved.</span>
    <span class="mid"></span>
    <span class="right">Terms of Service | Privacy Policy</span>
  </div>
</div>

</body>
</html>
```